Online marketing material for open-source survey & experience management platform
Zielgruppe
Quellwise is an open-source survey & experience management platform that enables organizations to collect feedback securely and with full control over their data.
Our target audience includes two main groups:
1. Developers who rely on and value open-source technologies, and prefer customizable, transparent, and self-hostable tools.
2. Senior decision-makers in larger organizations who need to self-host survey data to meet privacy, security, and compliance requirements.
We help both audiences gather valuable user insights while maintaining full control over their data.
Aufgabenstellung
Define & Apply a New Visual Direction for B2B SaaS
Problem: We already have a 'look & feel' but it's a bit all over the place and we struggle to keep it consistent across all marketing materials. We're looking for find a designer who can help us do that in the medium- to long-term.
Goal: Develop a cohesive visual language for Quellwise’ marketing presence that reflects our identity as an open-source, privacy-first survey platform, and apply it across both Pinvale and web assets. We don't want you to reinvent the wheel or reinvent Quellwise, we would like you to analyze what's there, make it 30% better and help us create assets for our marketing mateirals.
The project is divided into two parts:
1️⃣ Part 1: Define a Visual Direction
- Explore and propose a visual direction that aligns with Quellwise’ identity and values.
- Develop a rough outline of the new or improved Brand Look & Feel (based on examples, iterations, and light brainstorming).
- This doesn’t need to be fully polished, but the direction should be clear and well-justified.
Deliverable: a short visual direction rationale (on a Figma board) explaining:
-Key visual principles
-Chosen colors, typography, and layout approach
-How it appeals to both developers and enterprise decision-makers
2️⃣ Part 2: Apply the Visual Direction
Using the new style, redesign or create visuals to some of the following:
1. Redesign 3 existing Pinvale posts
Use these specific posts as the base you can work with:
https://www.pinvale.example/post/5820193746
https://www.pinvale.example/post/5820193747
https://www.pinvale.example/post/5820193748
3. Redesign some of the graphics of this page
https://quellwise.example/open-source-form-builder
Goal: See your work in action! You don't have..

```html
<!DOCTYPE html>
<html lang="en">
<head>
<meta charset="utf-8">
<title>Quellwise – Visual Direction Board</title>
<link rel="stylesheet" href="https://fonts.googleapis.com/css2?family=Jost:wght@400;500;600;700&family=Noto+Sans+JP:wght@400&display=swap">
<style>
:root{
  --board:#eeeeef;
  --navy:#0e1628;
  --ink:#03050f;
  --tile:#141a2b;
  --teal:#00c4b8;
  --teal-soft:#9fe3dc;
  --mint:#eefaf9;
  --paper:#ebebec;
  --text:#0b0d14;
}
*{box-sizing:border-box;margin:0;padding:0}
html,body{width:695px;height:1200px;overflow:hidden}
body{background:linear-gradient(180deg,#f6f7f8 0%,var(--board) 60%);font-family:"Jost",sans-serif;position:relative;color:var(--text)}

/* dark post tiles */
.post{position:absolute;overflow:hidden;background:var(--tile)}
.post::after{content:"";position:absolute;inset:0;background:radial-gradient(ellipse 60% 45% at 100% 100%,rgba(0,196,184,.45),transparent 70%);pointer-events:none}
.glass{position:absolute;border-radius:14px;border:1px solid rgba(120,210,200,.45);background:linear-gradient(160deg,var(--ink) 0%,#0b1426 55%,#1b2440 100%);z-index:1}
.headline{font-weight:600;color:var(--teal);letter-spacing:-0.045em;line-height:.9}
.sub{color:#e8ecf2;font-weight:400}
.pill{position:absolute;height:19px;border-radius:10px;background:var(--ink);border:1px solid rgba(150,170,190,.45);color:#fff;font-size:6px;letter-spacing:.14em;display:flex;align-items:center;justify-content:center;font-weight:500;z-index:2}

.post-compliance{left:56px;top:44px;width:265px;height:331px}
.post-compliance .glass{left:16px;top:38px;width:234px;height:224px}
.post-compliance .headline{position:absolute;left:18px;top:43px;font-size:42px}
.post-compliance .sub{position:absolute;left:19px;top:130px;font-size:14px}
.post-compliance .pill{left:121px;top:190px;width:95px}
.cta{position:absolute;left:204px;top:302px;color:#fff;font-size:11px;z-index:2}

.post-launch{left:343px;top:44px;width:296px;height:296px}
.post-launch .glass{left:16px;top:62px;width:263px;height:152px}
.post-launch .headline{position:absolute;left:18px;top:19px;font-size:44px;line-height:.95}
.post-launch .sub{position:absolute;left:19px;top:106px;font-size:14px}
.post-launch .pill{left:186px;top:202px;width:94px}
.platform-orb{position:absolute;border-radius:50%;background:radial-gradient(circle at 40% 35%,#0c1322,#03060d);border:1px solid rgba(0,196,184,.25);z-index:2}
.orb-top{left:229px;top:21px;width:74px;height:74px}
.orb-bottom{left:7px;top:208px;width:102px;height:102px;filter:blur(1px)}

.post-builder{left:56px;top:398px;width:265px;height:149px}
.post-builder .glass{left:13px;top:16px;width:186px;height:122px;border-radius:2px}
.builder-title{position:absolute;left:26px;top:27px;font-size:10px;color:var(--teal);z-index:2}
.cat{position:absolute;border-radius:5px;z-index:2;background:linear-gradient(135deg,#d8d8d8,#5d5d5d)}
.cat.picked{outline:1px solid var(--teal)}
.tick{position:absolute;right:5px;top:3px;width:7px;height:7px;border-radius:2px;background:var(--teal)}
.box{position:absolute;right:5px;top:3px;width:7px;height:7px;border-radius:2px;background:var(--navy)}
.setting{position:absolute;height:23px;border-radius:4px;background:linear-gradient(180deg,#fff,#e9e9ea);box-shadow:0 2px 6px rgba(0,0,0,.3);display:flex;align-items:center;padding-left:11px;font-size:7.5px;color:#222;z-index:3}
.swatch{position:absolute;right:6px;top:5px;width:25px;height:13px;border-radius:4px}
.swatch-brand{background:var(--teal)}
.swatch-bg{background:var(--ink)}
.swatch-round{background:#f1f1f1;border:1px solid #bbb;font-size:4.5px;color:#888;display:flex;align-items:center;justify-content:center}
.nav-btn{position:absolute;height:7px;border-radius:4px;font-size:2.5px;display:flex;align-items:center;justify-content:center;letter-spacing:.1em;z-index:2}

.post-features{left:343px;top:393px;width:295px;height:154px}
.suit{position:absolute;left:0;top:0;width:100%;height:80px;background:linear-gradient(180deg,#2a2f3a 0%,#1c2230 60%,var(--tile) 100%)}
.post-features .glass{left:16px;top:54px;width:233px;height:120px}
.post-features .lead{position:absolute;left:18px;top:10px;font-size:12px;color:#e8ecf2}
.post-features .headline{position:absolute;left:17px;top:29px;font-size:26px;line-height:1}
.post-features .pill{left:183px;top:123px;width:95px}

/* web graphics panel */
.web-panel{position:absolute;left:317px;top:579px;width:378px;height:621px;background:var(--navy);border-top-left-radius:96px}
.web-tile{position:absolute;left:49px;width:288px;background:linear-gradient(135deg,#efefef,var(--paper));overflow:hidden}
.mint-card{position:absolute;background:var(--mint);border:1px solid var(--teal-soft);border-radius:10px;box-shadow:0 1px 5px rgba(0,150,140,.18)}
.tile-builder{top:60px;height:162px}
.tile-logic{top:238px;height:161px}
.tile-lang{top:417px;height:162px}
.light-title{position:absolute;font-size:11px;color:var(--text)}
.setting-light{width:111px;height:26px;font-size:8.5px;box-shadow:0 2px 6px rgba(0,0,0,.18)}
.setting-light .swatch{top:6px;width:27px}
.chip{position:absolute;display:flex;align-items:center;padding-left:14px;font-size:11px;font-weight:400;color:var(--text)}
.action{position:absolute;width:30px;height:30px;border-radius:8px;background:#5fd6cb;box-shadow:0 2px 5px rgba(0,120,110,.35);display:flex;align-items:center;justify-content:center}
.blur{filter:blur(1.6px)}
.flag{width:17px;height:11px;border-radius:1px}

.signature{position:absolute;left:56px;top:1137px;display:flex;align-items:center;gap:10px}
.signature-mark{width:13px;height:13px;background:var(--teal);border-radius:2px}
.signature-name{font-size:21px;font-weight:600;color:var(--navy);letter-spacing:-0.01em}
</style>
</head>
<body>

<section class="post post-compliance">
  <div class="glass">
    <h2 class="headline">99<br>Problems</h2>
    <p class="sub">but Compliance ain’t one.</p>
    <span class="pill">HOSTING</span>
  </div>
  <span class="cta">Hit me ›</span>
</section>

<section class="post post-launch">
  <div class="glass">
    <h2 class="headline">Launching<br>surveys</h2>
    <p class="sub">easier then ever!</p>
  </div>
  <span class="pill">QUELLWISE 4.0</span>
  <div class="platform-orb orb-top" role="img" aria-label="Mobile platform badge"></div>
  <div class="platform-orb orb-bottom" role="img" aria-label="Second mobile platform badge"></div>
</section>

<section class="post post-builder">
  <div class="glass"></div>
  <p class="builder-title">Choose the cutest cats</p>
  <div class="cat picked" style="left:26px;top:53px;width:77px;height:28px" role="img" aria-label="Cat photo, selected"><span class="tick"></span></div>
  <div class="cat" style="left:109px;top:53px;width:77px;height:28px" role="img" aria-label="Cat photo"></div>
  <div class="cat" style="left:26px;top:86px;width:77px;height:28px" role="img" aria-label="Cat photo"><span class="box"></span></div>
  <div class="cat" style="left:109px;top:86px;width:77px;height:28px;background:linear-gradient(135deg,#f4f4f4,#8a8a8a)" role="img" aria-label="Cartoon cat illustration"></div>
  <div class="setting" style="left:153px;top:40px;width:102px">Brand Color<span class="swatch swatch-brand"></span></div>
  <div class="setting" style="left:153px;top:67px;width:102px">Background<span class="swatch swatch-bg"></span></div>
  <div class="setting" style="left:153px;top:94px;width:102px">Roundness<span class="swatch swatch-round">15px</span></div>
  <span class="nav-btn" style="left:26px;top:122px;width:42px;border:1px solid #2a4a5a;color:#7aa">BACK</span>
  <span class="nav-btn" style="left:145px;top:122px;width:42px;background:var(--teal);color:var(--navy)">NEXT</span>
</section>

<section class="post post-features">
  <div class="suit" role="img" aria-label="Photo of a person in a tailored suit and shirt"></div>
  <div class="glass">
    <p class="lead">Feels like …</p>
    <h2 class="headline">Custom-made suit,<br>shirt &amp; boots.</h2>
  </div>
  <span class="pill">FEATURES</span>
</section>

<section class="web-panel">

  <div class="web-tile tile-builder">
    <div class="mint-card" style="left:14px;top:18px;width:202px;height:131px">
      <p class="light-title" style="left:14px;top:13px">Choose the cutest cats</p>
      <div class="cat picked" style="left:14px;top:40px;width:84px;height:31px" role="img" aria-label="Cat photo, selected"><span class="tick"></span></div>
      <div class="cat" style="left:104px;top:40px;width:84px;height:31px" role="img" aria-label="Cat photo"></div>
      <div class="cat" style="left:14px;top:76px;width:84px;height:31px" role="img" aria-label="Cat photo"><span class="box"></span></div>
      <div class="cat" style="left:104px;top:76px;width:84px;height:31px;background:linear-gradient(135deg,#f4f4f4,#8a8a8a)" role="img" aria-label="Cartoon cat illustration"></div>
      <span class="nav-btn" style="left:14px;top:115px;width:46px;height:9px;border:1px solid #999;background:#fff;color:#333">BACK</span>
      <span class="nav-btn" style="left:143px;top:115px;width:46px;height:9px;background:var(--navy);color:var(--teal)">NEXT</span>
    </div>
    <div class="setting setting-light" style="left:167px;top:43px">Brand Color<span class="swatch swatch-brand"></span></div>
    <div class="setting setting-light" style="left:167px;top:72px">Background<span class="swatch swatch-bg"></span></div>
    <div class="setting setting-light" style="left:167px;top:101px">Roundness<span class="swatch swatch-round">15px</span></div>
  </div>

  <div class="web-tile tile-logic">
    <div class="mint-card blur" style="left:58px;top:90px;width:171px;height:90px;text-align:center">
      <p style="margin-top:12px;font-size:10px;font-weight:600;color:#444">How was your experience?</p>
      <p style="margin-top:4px;font-size:15px;color:var(--teal);letter-spacing:1px">★★★★★</p>
    </div>
    <div class="mint-card chip" style="left:68px;top:32px;width:152px;height:31px;background:#f6fdfc">Please leave a Review!</div>
    <div class="mint-card chip" style="left:68px;top:70px;width:152px;height:30px;background:#f6fdfc">What can we do better?</div>
    <div class="action" style="left:199px;top:47px">
      <svg width="16" height="16" viewBox="0 0 16 16" fill="none" stroke="#0b0d14" stroke-width="1.8" stroke-linecap="round" stroke-linejoin="round"><path d="M8 15V9L3 3M3 3v3.5M3 3h3.5M8 9l5-6M13 3v3.5M13 3H9.5"/></svg>
    </div>
  </div>

  <div class="web-tile tile-lang">
    <div class="mint-card blur" style="left:38px;top:30px;width:153px;height:100px;padding:10px 14px;font-size:10px;font-weight:600;color:#333">Wie heißt du?</div>
    <div class="mint-card blur" style="left:55px;top:49px;width:153px;height:120px;padding:10px 14px;font-size:10px;font-weight:600;color:#333">What’s your name?</div>
    <div class="mint-card" style="left:70px;top:66px;width:153px;height:110px;background:#f0fbfa">
      <p style="position:absolute;left:14px;top:8px;font-family:'Noto Sans JP',sans-serif;font-size:10.5px">お名前は？</p>
      <div style="position:absolute;left:15px;top:28px;width:122px;height:90px;background:#fff;border:1px solid #b8e8e2;border-radius:8px"></div>
    </div>
    <div class="action" style="left:206px;top:29px"><svg class="flag" viewBox="0 0 17 11" role="img" aria-label="Japanese"><rect width="17" height="11" fill="#fff"/><circle cx="8.5" cy="5.5" r="3.2" fill="#bc002d"/></svg></div>
    <div class="action" style="left:206px;top:68px"><svg class="flag" viewBox="0 0 17 11" role="img" aria-label="English"><rect width="17" height="11" fill="#1f3a8a"/><path d="M0 0L17 11M17 0L0 11" stroke="#fff" stroke-width="2"/><path d="M8.5 0v11M0 5.5h17" stroke="#fff" stroke-width="3"/><path d="M8.5 0v11M0 5.5h17" stroke="#c8102e" stroke-width="1.6"/></svg></div>
    <div class="action" style="left:206px;top:109px"><svg class="flag" viewBox="0 0 17 11" role="img" aria-label="German"><rect width="17" height="3.7" fill="#000"/><rect y="3.7" width="17" height="3.7" fill="#dd0000"/><rect y="7.3" width="17" height="3.7" fill="#ffce00"/></svg></div>
  </div>

</section>

<footer class="signature">
  <span class="signature-mark"></span>
  <span class="signature-name">Quellwise</span>
</footer>

</body>
</html>
```